Mardolin construction chemical business need advertisement

We need an advertisement as building signboard for a new company called "Mardolin"-meaning truly effective, value added building solution.
-we source the best and effective products around the world that suit the local climate conditions
- we carry varieties of quality construction chemicals products that are cost effective and suitable for any size of budget and project and even for home user DIY .
- we provide consultation and system to solve any building problems. e.g. tiling system, waterproofing system, concrete repair system, green roof system
- We provide products training and waterproofing solutions to our clients and applicators that use our products
-By utilising our products and services, will leverage the value of the properties and protect your investment.
-our mission- to provide consultancy, services to repair, to restpre and to add avlue to properties throughout the lifecycle of the building resulting in greater whole value hence not limited to develiper but to end user protecting their investment with the quality products and services we provide.
- our philosophy-"Passion towards commitment, quality, knowledge, good practice and result.
- we need the advertisement to be easily understand by End user and contractor of the service and product we provide to solve their problem
- yet also look professional to designer and architect
end user, contractor, builder, designer, achitect
Business
- -Please create a slogan, easily to understand at one glance of what type of service and products we provide.
- -less wording, the advertisement will be put at the building
- -Strong message to explain our business

```html
<!DOCTYPE html>
<html lang="en">
<head>
<meta charset="utf-8">
<title>Mardolin Construction Chemical – Restoration</title>
<link rel="stylesheet" href="https://fonts.googleapis.com/css2?family=Lato:wght@400;700&family=Oswald:wght@300;400;500&display=swap">
<style>
  :root {
    --sky: #7ecde8;
    --brand-blue: #2aa6d6;
    --ink: #111111;
    --white: #ffffff;
    --page-bg: #e9e9e9;
    --footer-grey: #555759;
    --photo-light: #eef5f9;
    --photo-mid: #b7cfdc;
    --photo-deep: #6f93a8;
  }
  * { margin: 0; padding: 0; box-sizing: border-box; }
  html, body {
    width: 1200px; height: 1200px; overflow: hidden;
    background: var(--page-bg);
  }
  .flyer {
    position: absolute; left: 181px; top: 12px;
    width: 855px; height: 1200px;
    transform: scale(0.98); transform-origin: top left;
    background: var(--white);
    overflow: hidden;
  }
  .hero-photo {
    position: absolute; left: 0; top: 0; width: 855px; height: 490px;
    background:
      radial-gradient(ellipse at 48% 42%, var(--photo-deep) 0%, var(--photo-mid) 28%, transparent 55%),
      linear-gradient(160deg, var(--white) 0%, var(--photo-light) 45%, var(--photo-mid) 100%);
  }
  .service-title {
    position: absolute; left: 0; top: 400px; height: 90px;
    display: inline-block;
    background: var(--white);
    font-family: "Oswald", sans-serif;
    font-size: 64px; line-height: 90px; letter-spacing: -1px;
    padding: 0 20px 0 50px; white-space: nowrap;
    transform: scaleX(0.84); transform-origin: left center;
  }
  .service-title .accent { color: var(--sky); font-weight: 500; }
  .service-title .main { color: var(--ink); font-weight: 300; }
  .slogan-band {
    position: absolute; left: 0; top: 500px; width: 855px; height: 126px;
    background: var(--sky);
    font-family: "Lato", sans-serif;
    box-shadow: 0 14px 14px -10px rgba(0,0,0,0.25);
  }
  .slogan-band .line-one {
    position: absolute; left: 43px; top: 14px;
    font-size: 50px; font-weight: 400; color: var(--ink); letter-spacing: 0.5px;
  }
  .slogan-band .line-two {
    position: absolute; left: 264px; top: 62px;
    font-size: 50px; font-weight: 700; color: var(--white);
  }
  .values-panel {
    position: absolute; left: -4px; top: 680px; width: 369px; height: 412px;
    border: 3px solid var(--sky); border-left: none;
    border-radius: 0 32px 32px 0;
    background: var(--white);
    box-shadow: 0 18px 16px -14px rgba(0,0,0,0.28);
  }
  .values-panel .brand-line {
    position: absolute; left: 46px; top: 36px;
    font-family: "Oswald", sans-serif; font-weight: 500;
    font-size: 28px; color: var(--brand-blue); white-space: nowrap;
  }
  .values-panel .product-line {
    position: absolute; left: 44px; top: 72px;
    font-family: "Lato", sans-serif; font-weight: 400;
    font-size: 60px; color: var(--ink); letter-spacing: 1px;
  }
  .values-list {
    position: absolute; left: 46px; top: 160px; list-style: none;
    font-family: "Lato", sans-serif; font-weight: 700;
    font-size: 36px; line-height: 35px; color: var(--ink);
  }
  .values-list li { position: relative; padding-left: 28px; margin-bottom: 10px; }
  .values-list li::before {
    content: ""; position: absolute; left: 0; top: 13px;
    width: 13px; height: 13px; border-radius: 50%; background: var(--sky);
  }
  .product-photo {
    position: absolute; left: 412px; top: 668px; width: 390px; height: 385px;
    background: radial-gradient(ellipse at 45% 50%, #ffffff 0%, #f1f1f1 50%, transparent 72%);
  }
  .call-line {
    position: absolute; left: 428px; top: 1070px;
    font-family: "Oswald", sans-serif; font-weight: 400;
    font-size: 42px; white-space: nowrap;
    transform: scaleX(0.8); transform-origin: left center;
  }
  .call-line .call { color: var(--sky); }
  .call-line .now { color: var(--ink); margin-right: 24px; }
  .call-line .number { color: var(--sky); }
  .footer-band {
    position: absolute; left: 0; bottom: 0; width: 855px; height: 35px;
    background: var(--footer-grey);
  }
</style>
</head>
<body>
  <main class="flyer">
    <div class="hero-photo" role="img" aria-label="Blue-toned model house resting on architectural blueprints"></div>

    <h1 class="service-title"><span class="accent">MARDOLIN</span> <span class="main">RESTORATION</span></h1>

    <section class="slogan-band">
      <p class="line-one">EVERYTHING YOU NEED</p>
      <p class="line-two">FROM START TO FINISH</p>
    </section>

    <section class="values-panel">
      <p class="brand-line">MARDOLIN CONSTRUCTION</p>
      <p class="product-line">CHEMICAL</p>
      <ul class="values-list">
        <li>Passion towards<br>commitment</li>
        <li>Quality</li>
        <li>knowledge</li>
        <li>Good practice</li>
      </ul>
    </section>

    <div class="product-photo" role="img" aria-label="Two white construction chemical buckets labelled Mardolin Construction Chemical"></div>

    <p class="call-line"><span class="call">CALL</span> <span class="now">NOW:</span><span class="number">XXX-XXXXX-XX</span></p>

    <div class="footer-band"></div>
  </main>
</body>
</html>
```